Book writer needs a Book Cover Design for 'Atomic Arms and the Law of States'

A Book Cover Design is required for a new book with a current working title of: 'Atomic Arms and the Law of States' plus subtitle something like: 'from the Harwick Atomic Conflict Panel via the Global Bench of Equity Advisory Opinion to contemporary developments'.

The book will be issued in three formats: hardback, paperback, and electronic.

The Editor of the book is Reginald Palfrey.

The finished size of the paperback front cover will be 15.2mm x 22.9mm. Initial thoughts about themes for the front cover include a nuclear explosion, and perhaps scales of justice, but designers have total freedom to propose ideas.

The back cover will have approximately 250 words of text, and a space at the bottom of about 37mm for publisher logo and ISBN barcode, The designer is free to suggest anything for the back cover.

No illustrations where the copyright is owned by someone else should be used, and the designer must be able to transfer exclusive copyright in the design to the client. The designer will be acknowledged in the book (unless the designer does not want to be).

The themes in the book are:
1. Harwick Atomic conflict Panel
2. Civic Bench Venture
3. Global Bench of Equity Advisory Opinion
4. Dissenting Judgment By Judge Tallisborne
5. Contemporary Activities (e.g. current case involving the Marshall Islands)

Target Market(s)

government decision makers taking decisions about nuclear weapons,iInternational lawyers, students of public international law,

Font styles to use
Serif

Requirements
Must have
• this is in the discretion of the designer
• Title, subtitle, editor (Reginald Palfrey)
Nice to have
• possibly images of nuclear explosion, effects of nuclear weapons, symbols for international law
Should not have
• in the discretion of the designer

```html
<!DOCTYPE html>
<html lang="en">
<head>
<meta charset="utf-8">
<title>Atomic Arms and the Law of States — Book Cover</title>
<link rel="stylesheet" href="https://fonts.googleapis.com/css2?family=Oswald:wght@300;400&family=Didact+Gothic&display=swap">
<style>
  :root {
    --night: #050100;
    --smoke: #1c0301;
    --ember: #5e0a02;
    --flame: #8c1604;
    --bronze: #b7a489;
    --bronze-light: #d6c6ab;
    --paper: #f1ece4;
  }
  html, body {
    margin: 0;
    padding: 0;
    width: 928px;
    height: 1200px;
    overflow: hidden;
    background: var(--night);
  }
  .cover {
    position: relative;
    width: 928px;
    height: 1200px;
    overflow: hidden;
    background: var(--night);
  }
  .cover__photo {
    position: absolute;
    inset: 0;
    background: linear-gradient(180deg,
      var(--night) 0%,
      var(--smoke) 18%,
      var(--ember) 40%,
      var(--flame) 58%,
      var(--ember) 76%,
      var(--smoke) 90%,
      var(--night) 100%);
  }
  .cover__editor {
    position: absolute;
    right: 102px;
    top: 84px;
    margin: 0;
    font-family: "Oswald", sans-serif;
    font-weight: 300;
    font-size: 62px;
    line-height: 1.08;
    letter-spacing: 0.07em;
    color: var(--bronze);
    text-align: right;
    white-space: nowrap;
  }
  .cover__editor span { display: block; }
  .cover__title {
    position: absolute;
    left: 100px;
    top: 56px;
    width: 230px;
    height: 860px;
    margin: 0;
  }
  .cover__title svg { display: block; }
  .title-line {
    font-family: "Oswald", sans-serif;
    font-weight: 300;
    font-size: 118px;
    fill: var(--bronze);
  }
  .cover__scales {
    position: absolute;
    left: 100px;
    top: 920px;
    width: 208px;
    height: 170px;
    background: var(--bronze);
    opacity: 0.8;
  }
  .cover__subtitle {
    position: absolute;
    left: 330px;
    top: 936px;
    width: 456px;
    margin: 0;
    font-family: "Didact Gothic", sans-serif;
    font-size: 23px;
    line-height: 27px;
    color: var(--paper);
  }
  .cover__subtitle span {
    display: block;
    text-align: justify;
    text-align-last: justify;
  }
</style>
</head>
<body>
  <main class="cover">
    <div class="cover__photo" role="img" aria-label="Photograph of a nuclear mushroom cloud glowing red and orange against a dark sky"></div>

    <p class="cover__editor"><span>REGINALD</span><span>PALFREY</span></p>

    <h1 class="cover__title">
      <svg width="230" height="860" viewBox="0 0 230 860" aria-label="Atomic Arms and the Law of States">
        <text class="title-line" transform="translate(90 860) rotate(-90)" textLength="856" lengthAdjust="spacingAndGlyphs">ATOMIC ARMS &amp;</text>
        <text class="title-line" transform="translate(212 860) rotate(-90)" textLength="856" lengthAdjust="spacingAndGlyphs">THE LAW OF STATES</text>
      </svg>
    </h1>

    <div class="cover__scales" role="img" aria-label="Scales of justice emblem in bronze"></div>

    <p class="cover__subtitle">
      <span>from the Harwick Atomic Conflict Panel</span>
      <span>via the Global Bench of Equity</span>
      <span>Advisory Opinion to</span>
      <span>contemporary developments</span>
    </p>
  </main>
</body>
</html>
```